Velmor Agritech, Inc. Business Card

We are joint venture hybrid vegetable seed company. We design & breed application specific products for fresh market and processing applications. We are looking for a business card that will have impact and convey elegance, excellence, high technology, and have enormous eye appeal. It needs to be unique in design and can incorporate photos, or symbols as the case may be.

I very much enjoy the minimalist approach to Quorlin's product designs. We would like to include a tag line in the business card: Breeding Success

Target Market(s)

We breed proprietary products that provide better solutions for growers, harvesters, packers, shippers, wholesalers, retailers, consumers, and processors. Regional seed distributors worldwide are our primary clients and then growers. We need to appeal first and foremost to the distributors who will be representing us and selling the products in their target markets.

Industry/Entity Type

Business

Requirements
Must have
• It will have a picture of a cluster of tomatoes on one side and the other side will include the logo, a tag line, our contact information, and a possibly a picture or symbol. I want the contact side to be edgy and convey elegance, solidity, and exclusivity.
Nice to have
• Surprise us with something special.
Should not have
• Card needs to work well with the green logo so it can't be diminished by the background color of the card.

```html
<!DOCTYPE html>
<html lang="en">
<head>
<meta charset="utf-8">
<title>Velmor Agritech, Inc. Business Card</title>
<link href="https://fonts.googleapis.com/css2?family=Roboto:wght@400;500;700&display=swap" rel="stylesheet">
<style>
  :root {
    --page-bg: #e9eaeb;
    --card-bg: #ffffff;
    --brand-green: #0d7a55;
    --brand-green-dark: #095c40;
    --ink: #1d1d1d;
    --ink-soft: #6b6b6b;
    --tomato-light: #e8432f;
    --tomato-dark: #9e120c;
  }
  * { margin: 0; padding: 0; box-sizing: border-box; }
  html, body { width: 1200px; height: 900px; overflow: hidden; }
  body {
    background: var(--page-bg);
    font-family: "Roboto", Arial, sans-serif;
    color: var(--ink);
    position: relative;
  }
  .card {
    position: absolute;
    top: 295px;
    width: 540px;
    height: 310px;
    background: linear-gradient(160deg, #ffffff 0%, #f4f5f5 100%);
    box-shadow: 0 6px 18px rgba(0,0,0,0.18);
    overflow: hidden;
  }
  .card--front { left: 40px; }
  .card--back { left: 620px; }
  .circuit { position: absolute; inset: 0; width: 100%; height: 100%; }
  .circuit line, .circuit polyline { stroke: var(--brand-green); stroke-width: 2; fill: none; }
  .circuit circle { fill: var(--brand-green); }

  .brand {
    position: absolute;
    display: flex;
    align-items: center;
    gap: 8px;
    color: var(--brand-green);
    font-weight: 700;
    white-space: nowrap;
  }
  .brand__dot { border-radius: 50%; background: var(--brand-green); }
  .card--front .brand { left: 26px; top: 52px; font-size: 21px; }
  .card--front .brand__dot { width: 14px; height: 14px; }
  .card--back .brand { left: 0; right: 0; top: 112px; justify-content: center; font-size: 38px; }
  .card--back .brand__dot { width: 22px; height: 22px; }

  .tagline {
    position: absolute;
    font-size: 14px;
    font-weight: 500;
    color: var(--ink);
    white-space: nowrap;
  }
  .card--front .tagline { left: 30px; top: 132px; font-size: 13px; }
  .card--back .tagline { left: 0; right: 0; top: 224px; text-align: center; font-size: 19px; font-weight: 400; }

  .person { position: absolute; right: 50px; top: 16px; text-align: right; line-height: 1.15; }
  .person__name { font-size: 19px; font-weight: 700; }
  .person__title { font-size: 12px; color: var(--ink-soft); margin-top: 20px; }

  .contacts { position: absolute; left: 36px; top: 220px; list-style: none; }
  .contacts li { display: flex; align-items: center; gap: 12px; font-size: 13px; color: #333; height: 25px; }
  .contacts svg { width: 14px; height: 14px; fill: #555; }

  .produce-photo {
    position: absolute;
    left: 308px; top: 150px;
    width: 232px; height: 160px;
    background: radial-gradient(ellipse at 45% 45%, var(--tomato-light) 0%, #c8231a 55%, var(--tomato-dark) 100%);
    border-radius: 60px 0 0 0;
  }
</style>
</head>
<body>

<section class="card card--front">
  <svg class="circuit" viewBox="0 0 540 310" aria-hidden="true">
    <line x1="0" y1="141" x2="26" y2="141"/>
    <polyline points="150,141 526,141 526,14"/>
    <circle cx="4" cy="141" r="5"/>
    <circle cx="189" cy="141" r="5"/>
    <circle cx="526" cy="14" r="5"/>
    <polyline points="295,141 295,48 490,48"/>
    <polyline points="8,141 8,265"/>
    <circle cx="8" cy="265" r="5"/>
    <polyline points="8,190 212,190 212,286 275,286"/>
    <circle cx="275" cy="286" r="5"/>
  </svg>

  <div class="brand"><span class="brand__name">Velmor Agritech, Inc.</span><span class="brand__dot"></span></div>
  <div class="tagline">Breeding Success</div>

  <div class="person">
    <div class="person__name">Your Name</div>
    <div class="person__title">Title</div>
  </div>

  <ul class="contacts">
    <li><svg viewBox="0 0 16 16"><path d="M3 5c0-1.5 2-2.5 5-2.5s5 1 5 2.5v1.5h-3v-1h-4v1H3zM2 8h12v6H2zM6 10h4v2H6z"/></svg>123 456 1234</li>
    <li><svg viewBox="0 0 16 16"><path d="M1 3h14v10H1zM2 4l6 5 6-5"/></svg>mail@email.com</li>
    <li><svg viewBox="0 0 16 16"><circle cx="8" cy="8" r="7"/></svg>www.velmoragri.com</li>
  </ul>

  <div class="produce-photo" role="img" aria-label="Photograph of a cluster of ripe red tomatoes on the vine"></div>
</section>

<section class="card card--back">
  <svg class="circuit" viewBox="0 0 540 310" aria-hidden="true">
    <line x1="0" y1="236" x2="140" y2="236"/>
    <circle cx="140" cy="236" r="5"/>
    <line x1="400" y1="236" x2="540" y2="236"/>
    <circle cx="400" cy="236" r="5"/>
  </svg>
  <div class="brand"><span class="brand__name">Velmor Agritech, Inc.</span><span class="brand__dot"></span></div>
  <div class="tagline">Breeding Success</div>
</section>

</body>
</html>
```